Ridge 4 Ridge Turbine Rentals Pty Ltd

We are a hire company based on the Gold Coast in Australia, we Hire out Generators to construction sites, music festivals, parties, fetes etc. Anywhere where power is required we can provide it.

Ridge 4 Ridge Turbine Rentals pty Ltd also provides all leads, distribution boards, Qualified Electricians to perform all connections. we offer refuelling services and mechanical services. 24Hr on call service - to an actual english speaking operator.

Slogan ''Power Anywhere Anytime"

Industry/Entity Type

Construction

Contact Information for Business Card

M: 0481265390
E: bookings@ridge4ridgeturbinerentals-example.com.au

```html
<!DOCTYPE html>
<html lang="en">
<head>
<meta charset="utf-8">
<title>Ridge 4 Ridge Turbine Rentals – Business Card</title>
<link href="https://fonts.googleapis.com/css2?family=Roboto:wght@300;700&display=swap" rel="stylesheet">
<style>
  :root {
    --stage: #ecebe8;
    --card-light: #e4e5ea;
    --card-light-deep: #d3d5dc;
    --panel: #f3f5f7;
    --brand-blue: #1a7fc0;
    --ink: #1b1d20;
    --night: #121314;
    --night-soft: #1b1c1e;
    --contact-text: #b9bcc2;
    --white: #ffffff;
  }
  * { box-sizing: border-box; margin: 0; padding: 0; }
  html, body {
    width: 1200px; height: 800px; overflow: hidden;
    background: var(--stage);
    font-family: "Roboto", Arial, sans-serif;
  }
  .canvas { position: relative; width: 1200px; height: 800px; }

  .card {
    position: absolute;
    width: 540px; height: 309px;
    overflow: hidden;
    box-shadow: 0 10px 28px rgba(0,0,0,0.16), 0 2px 6px rgba(0,0,0,0.1);
  }
  .card--front { left: 610px; top: 90px; }
  .card--back  { left: 70px;  top: 400px; }

  .texture {
    position: absolute; inset: 0;
    background: linear-gradient(135deg, var(--card-light) 0%, var(--card-light-deep) 55%, var(--card-light) 100%);
  }

  /* Front */
  .front-panel {
    position: absolute;
    left: 82px; top: 68px; width: 376px; height: 172px;
    background: var(--panel);
    display: flex; align-items: center; justify-content: center;
  }
  .front-tab {
    position: absolute;
    left: 258px; width: 166px; height: 22px;
    background: var(--brand-blue);
  }
  .front-tab--top { top: 50px; }
  .front-tab--bottom { top: 230px; }

  .brand-name {
    font-weight: 700;
    color: var(--ink);
    text-transform: uppercase;
    text-align: center;
    line-height: 1.15;
    letter-spacing: 0.02em;
  }
  .brand-name--front { font-size: 26px; }
  .brand-name--back { font-size: 17px; }
  .brand-name span { display: block; }
  .brand-name .brand-sub { font-size: 0.56em; letter-spacing: 0.12em; }

  /* Back */
  .back-light {
    position: absolute; left: 0; top: 0; width: 200px; height: 100%;
  }
  .back-band {
    position: absolute;
    left: 0; top: 84px; width: 200px; height: 108px;
    background: var(--panel);
    display: flex; align-items: center; justify-content: center;
  }
  .back-dark {
    position: absolute; left: 200px; top: 0; right: 0; height: 100%;
    background: linear-gradient(160deg, var(--night-soft), var(--night));
  }
  .contact-list { position: absolute; left: 180px; top: 140px; list-style: none; }
  .contact-item {
    display: flex; align-items: center;
    height: 32px; margin-bottom: 6px;
  }
  .contact-icon {
    width: 32px; height: 32px; flex: none;
    background: var(--brand-blue);
    display: flex; align-items: center; justify-content: center;
  }
  .contact-icon svg { width: 16px; height: 16px; }
  .contact-text {
    margin-left: 12px;
    font-weight: 300;
    font-size: 11px;
    color: var(--contact-text);
    white-space: nowrap;
  }
</style>
</head>
<body>
<main class="canvas">

  <section class="card card--front" aria-label="Business card front">
    <div class="texture" role="img" aria-label="Soft grey faceted polygon texture"></div>
    <div class="front-tab front-tab--top"></div>
    <div class="front-panel">
      <p class="brand-name brand-name--front"><span>Ridge 4 Ridge</span><span class="brand-sub">Turbine Rentals</span></p>
    </div>
    <div class="front-tab front-tab--bottom"></div>
  </section>

  <section class="card card--back" aria-label="Business card back">
    <div class="texture back-light" role="img" aria-label="Soft grey faceted polygon texture"></div>
    <div class="back-band">
      <p class="brand-name brand-name--back"><span>Ridge 4 Ridge</span><span class="brand-sub">Turbine Rentals</span></p>
    </div>
    <div class="back-dark"></div>
    <ul class="contact-list">
      <li class="contact-item">
        <span class="contact-icon">
          <svg viewBox="0 0 24 24" aria-hidden="true"><path fill="#fff" d="M6.6 10.8a15.1 15.1 0 0 0 6.6 6.6l2.2-2.2c.3-.3.7-.4 1-.2 1.1.4 2.3.6 3.6.6.6 0 1 .4 1 1V20c0 .6-.4 1-1 1C10.6 21 3 13.4 3 4c0-.6.4-1 1-1h3.5c.6 0 1 .4 1 1 0 1.3.2 2.5.6 3.6.1.3 0 .7-.2 1z"/></svg>
        </span>
        <span class="contact-text">0481265390</span>
      </li>
      <li class="contact-item">
        <span class="contact-icon">
          <svg viewBox="0 0 24 24" aria-hidden="true" fill="none" stroke="#fff" stroke-width="1.6"><circle cx="12" cy="12" r="9"/><ellipse cx="12" cy="12" rx="4" ry="9"/><line x1="3" y1="12" x2="21" y2="12"/><line x1="4.5" y1="7.5" x2="19.5" y2="7.5"/><line x1="4.5" y1="16.5" x2="19.5" y2="16.5"/></svg>
        </span>
        <span class="contact-text">bookings@ridge4ridgeturbinerentals-example.com.au</span>
      </li>
    </ul>
  </section>

</main>
</body>
</html>
```